GILDED BRICKWORK: THE DEPENDABLE ROUTE WHEREBY MODEST HOUSING FLIPS YIELD HANDSOME RETURNS

I am looking for a book cover design for my new E-Book.

My idea for the design is a pin board with before and after photos of our properties pinned on it (example attached). I have also attached some photos to use.

PLEASE SUBMIT OTHER DESIGNS ALSO AS THIS WAS JUST AN IDEA BUT I AM OPEN TO OTHER IDEAS ALSO.

Page size is 5x7 inches

Font styles to use
Serif
Sans Serif

Colors
0255a3
3176b5
85acd3
85cae6
33a6d7
0392cd
9bcb3c
abd036
ec1f27

```html
<!DOCTYPE html>
<html lang="en">
<head>
<meta charset="utf-8">
<title>Gilded Brickwork — Marcus Ellerby</title>
<link href="https://fonts.googleapis.com/css2?family=Bebas+Neue&family=Josefin+Sans:wght@600;700&family=Roboto+Slab:wght@800;900&family=Courier+Prime&display=swap" rel="stylesheet">
<style>
  :root {
    --frame: #000000;
    --cover-top: #dfe4e5;
    --cover-bottom: #cfd6d8;
    --ink: #111111;
    --accent-red: #b3121a;
    --paint-blue: #1f7ccc;
    --paint-deep: #0c5fa8;
    --photo-border: #ffffff;
    --label: #ffffff;
  }
  * { box-sizing: border-box; margin: 0; padding: 0; }
  html, body { width: 923px; height: 1200px; overflow: hidden; background: var(--frame); }
  .canvas { position: relative; width: 923px; height: 1200px; background: var(--frame); }
  .cover {
    position: absolute; left: 55px; top: 28px; width: 817px; height: 1145px;
    background: linear-gradient(180deg, var(--cover-top), var(--cover-bottom));
    overflow: hidden;
  }
  .paint-stroke {
    position: absolute; left: 14px; top: 185px; width: 356px; height: 665px;
    background: linear-gradient(180deg, var(--paint-blue) 0%, #2a86d4 60%, var(--paint-deep) 100%);
    border-radius: 6px 10px 4px 8px;
  }
  .author {
    position: absolute; top: 70px; left: 0; width: 100%; text-align: center;
    font-family: "Josefin Sans", sans-serif; font-weight: 700; font-size: 31px;
    letter-spacing: 5px; color: var(--ink);
  }
  .title-main {
    position: absolute; top: 107px; left: 0; width: 100%; text-align: center;
    font-family: "Bebas Neue", sans-serif; font-size: 178px; line-height: 1;
    letter-spacing: 6px; color: var(--ink);
  }
  .title-accent {
    position: absolute; top: 253px; right: 22px;
    font-family: "Roboto Slab", serif; font-weight: 900; font-size: 68px; line-height: 1;
    letter-spacing: 3px; color: var(--accent-red);
  }
  .photo {
    position: absolute; border: 6px solid var(--photo-border);
    box-shadow: 0 2px 6px rgba(0,0,0,.35);
  }
  .photo-label {
    position: absolute; font-family: "Courier Prime", monospace; color: var(--label);
    letter-spacing: 3px; text-shadow: 0 1px 3px rgba(0,0,0,.6);
  }
  .photo--after-cottage { left: 56px; top: 408px; width: 404px; height: 277px;
    background: linear-gradient(180deg, #7fa9c8 0%, #4d6b3e 45%, #3e7a2c 100%); }
  .photo--before-cottage { left: 460px; top: 339px; width: 271px; height: 265px;
    background: linear-gradient(180deg, #a9c6da 0%, #6c7a5a 40%, #6e6a5e 100%); }
  .photo--before-duplex { left: 502px; top: 604px; width: 274px; height: 194px; transform: rotate(2deg);
    background: linear-gradient(180deg, #9dbad0 0%, #c9c3b4 50%, #7a7b73 100%); }
  .photo--after-duplex { left: 314px; top: 692px; width: 300px; height: 210px; transform: rotate(-1.5deg);
    background: linear-gradient(180deg, #9cb8d6 0%, #3e4a66 45%, #4c5a43 100%); }
  .photo--after-cottage .photo-label { left: 0; right: 0; bottom: 6px; text-align: center; font-size: 26px; }
  .photo--before-cottage .photo-label { right: 40px; bottom: 6px; font-size: 26px; }
  .photo--before-duplex .photo-label { right: 10px; bottom: 4px; font-size: 17px; }
  .photo--after-duplex .photo-label { left: 8px; bottom: 2px; font-size: 32px; }
  .subtitle {
    position: absolute; top: 962px; left: 0; width: 100%; text-align: center;
    font-family: "Roboto Slab", serif; font-weight: 800; font-size: 29px; line-height: 33px;
    letter-spacing: 1px; color: var(--ink);
    text-shadow: 0 0 3px rgba(255,255,255,.9);
  }
  .imprint {
    position: absolute; top: 1104px; left: 0; width: 100%; text-align: center;
    font-family: "Josefin Sans", sans-serif; font-weight: 600; font-size: 18px;
    letter-spacing: 3px; color: var(--ink);
  }
</style>
</head>
<body>
<div class="canvas">
  <div class="cover">
    <div class="paint-stroke" role="img" aria-label="Blue paint roller stroke running down the left side of the cover"></div>
    <div class="author">MARCUS ELLERBY</div>
    <div class="title-main">GILDED</div>
    <div class="title-accent">BRICKWORK</div>

    <div class="photo photo--before-cottage" role="img" aria-label="Before photo: overgrown cottage yard with carport">
      <span class="photo-label">Before</span>
    </div>
    <div class="photo photo--after-cottage" role="img" aria-label="After photo: renovated cottage with deck, lawn and stepping stones">
      <span class="photo-label">After</span>
    </div>
    <div class="photo photo--before-duplex" role="img" aria-label="Before photo: two-storey house with cream cladding and garages">
      <span class="photo-label">Before</span>
    </div>
    <div class="photo photo--after-duplex" role="img" aria-label="After photo: two-storey house repainted in navy with dark garage doors">
      <span class="photo-label">after</span>
    </div>

    <div class="subtitle">THE DEPENDABLE ROUTE WHEREBY<br>MODEST HOUSING FLIPS YIELD<br>HANDSOME RETURNS</div>
    <div class="imprint">ELLERBY HOUSE • BUILD YOUR EQUITY</div>
  </div>
</div>
</body>
</html>
```